依頼詳細
集合場所が分かりにくいので、周辺が混みあうときには2~3本立てて、その目印に使います。なるべく目立つ印象で、明るく楽しい感じが伝わってくるものが良いです。写真も添付しますのでご利用ください。
記載項目
記載項目:鳥取砂丘でパラグライダー体験!
サイズ:一般的なのぼりのサイズ(600×1800ミリ)
希望イメージ
シンプル 複雑
単色 カラフル
暗い 明るい
日常 高級
遊び心 厳粛
未来的 伝統的
女性的 男性的
希望する色
青、黄、オレンジ
納品ファイル
• 高解像度JPG (.jpg)
• イラストレーター形式 (.ai)
補足説明
当方のHPは、
http://mina.kotoha.info/
になります。
画像等は、参考にしていただければと思います。
■ 選んだ理由

今回かなり悩みました。
期間をじっくり置いて、いろいろな視点ですべての作品を見させていただいた中で、写真を大きくはっきり使っていただいたのと、その配置が絶妙で、文字の自由度が大きくなる点を評価しました。
写真の切り取り方が良かったと思います。

■ 提案者全員のお礼・コメント

多数のご提案まことにありがとうございました。
甲乙つけがたいものが多くて、自分がどうこう評価するにはおこがましい感覚を受けながらも、みなさまの作品をじっくり拝見して、吟味させていただきました。
写真以外の可能性も感じたり、キャラや文字を面白くデフォルメしてくださったり、斬新な構図を見せてくださったり、う~んと感心ばかりしていました。
当方、まったくデザインに関して素人にも関わらず、いろいろなことを勉強させていただいたように思います。
皆さまの貴重な時間を、このたびは本当にありがとうございました。m(_ _)m

```html
<!DOCTYPE html>
<html lang="ja">
<head>
<meta charset="utf-8">
<title>鳥取砂丘でパラグライダー体験!</title>
<link href="https://fonts.googleapis.com/css2?family=M+PLUS+1p:wght@800;900&display=swap" rel="stylesheet">
<style>
  :root {
    --page: #ffffff;
    --sky-top: #1e8fc9;
    --sky-mid: #27b3d6;
    --sky-low: #6fd0e4;
    --sand-light: #f1eee9;
    --sand-shadow: #c9c2b8;
    --photo-grey: #9aa3ab;
    --photo-sky: #8fc4e0;
    --photo-warm: #d9a27a;
    --ink: #12263f;
    --title: #ffffff;
  }
  * { margin: 0; padding: 0; box-sizing: border-box; }
  html, body {
    width: 900px; height: 1200px; overflow: hidden;
    background: var(--page);
  }
  .nobori {
    position: absolute;
    left: 171px; top: 6px;
    width: 558px; height: 1173px;
    overflow: hidden;
    background: linear-gradient(180deg, var(--sky-top) 0%, var(--sky-mid) 45%, var(--sky-low) 72%, var(--sand-light) 76%);
    font-family: "M PLUS 1p", sans-serif;
  }
  .sand-field {
    position: absolute; left: 0; right: 0; bottom: 0; height: 300px;
    background: linear-gradient(180deg, var(--sand-light) 0%, var(--sand-shadow) 55%, var(--sand-light) 100%);
  }
  .photo-circle {
    position: absolute; border-radius: 50%;
  }
  .photo-sky-top   { left: 100px; top: 10px;  width: 150px; height: 150px; background: radial-gradient(circle at 40% 40%, #c9e4f2, var(--photo-sky)); }
  .photo-glider-1  { left: 180px; top: 170px; width: 190px; height: 190px; background: radial-gradient(circle at 50% 40%, #b9c2c9, var(--photo-grey)); }
  .photo-children  { left: 330px; top: 420px; width: 230px; height: 230px; background: radial-gradient(circle at 50% 50%, #e6d2bd, var(--photo-warm) 70%, #8fb1c7); }
  .photo-flag      { left: 105px; top: 630px; width: 180px; height: 180px; background: linear-gradient(180deg, #a9d3ea 0%, #e2a058 60%, #e8dfd2 100%); }
  .photo-glider-2  { left: 370px; top: 800px; width: 200px; height: 200px; background: radial-gradient(circle at 50% 40%, #b4bcc3, var(--photo-grey)); }
  .title-lead, .title-main {
    position: absolute;
    writing-mode: vertical-rl;
    text-orientation: upright;
    color: var(--title);
    font-weight: 900;
    white-space: nowrap;
    -webkit-text-stroke: 5px var(--ink);
    paint-order: stroke fill;
    text-shadow: 4px 5px 0 var(--ink);
  }
  .title-lead {
    left: 385px; top: 22px;
    font-size: 44px; letter-spacing: -2px;
    transform: rotate(-12deg) scaleX(1.5);
    transform-origin: top center;
  }
  .title-main {
    left: 190px; top: 180px;
    font-size: 94px; letter-spacing: -6px; line-height: 1;
    transform: rotate(-8deg) scaleX(1.75);
    transform-origin: top center;
  }
</style>
</head>
<body>
  <div class="nobori">
    <div class="sand-field" role="img" aria-label="風紋が広がる鳥取砂丘の写真"></div>
    <div class="photo-circle photo-sky-top" role="img" aria-label="青空を飛ぶパラグライダーの写真"></div>
    <div class="photo-circle photo-glider-1" role="img" aria-label="砂丘上空を滑空するパラグライダーの写真"></div>
    <div class="photo-circle photo-children" role="img" aria-label="ハーネスを付けた子どもたちの写真"></div>
    <div class="photo-circle photo-flag" role="img" aria-label="砂丘に広げたカラフルなキャノピーの写真"></div>
    <div class="photo-circle photo-glider-2" role="img" aria-label="赤いパラグライダーで飛ぶ人の写真"></div>
    <h2 class="title-lead">鳥取砂丘で</h2>
    <h1 class="title-main">パラグライダー体験!</h1>
  </div>
</body>
</html>
```